Postcard Design

The company is a global consulting company that is focusing on start-up business solutions and trade show management in the USA and overseas. The company web site is www.veltrapro.com.

We need the postcard to inform previous clients and industry contacts about our company.

We would like to see a design that includes the main colors of the logo, as well as the global consulting aspect.

The logo is attached.
Updates

Target Market(s)

Start-up business and trade shows element

Industry/Entity Type

Business

Requirements
Must have
• The logo needs to be included,

The international and start-up business ideas should be implemented.

```html
<!DOCTYPE html>
<html lang="en">
<head>
<meta charset="utf-8">
<title>Veltra Pro Postcard</title>
<link rel="stylesheet" href="https://fonts.googleapis.com/css2?family=Source+Sans+3:wght@400;600;700&display=swap">
<style>
  :root {
    --band-blue: #1570b8;
    --brand-navy: #1a4f86;
    --strip-red: #ec2227;
    --strip-red-ink: #7a1014;
    --strip-yellow: #f9b51b;
    --strip-yellow-ink: #4a3408;
    --strip-sky: #4fc3ee;
    --strip-sky-ink: #1d3d55;
    --paper: #ffffff;
    --ink: #3d3d3d;
    --stamp-red: #d9473b;
    --stamp-cream: #f3e3d6;
  }
  * { margin: 0; padding: 0; box-sizing: border-box; }
  html, body { width: 1200px; height: 917px; overflow: hidden; background: var(--paper); }
  body { font-family: "Source Sans 3", "Myriad Pro", sans-serif; position: relative; }

  .postcard { position: relative; width: 1200px; height: 917px; background: var(--paper); }

  .header-band {
    position: absolute; left: 0; top: 0; width: 926px; height: 286px;
    background: var(--band-blue);
  }
  .brand-box {
    position: absolute; left: 21px; top: 26px; width: 234px; height: 233px;
    background: var(--paper);
    display: flex; flex-direction: column; align-items: center; justify-content: center; gap: 18px;
  }
  .brand-mark { width: 70px; height: 70px; background: var(--brand-navy); }
  .brand-name { color: var(--brand-navy); font-weight: 600; font-size: 38px; line-height: 1; }

  .contact-strip {
    position: absolute; top: 0; height: 286px;
    display: flex; align-items: center; justify-content: center;
  }
  .contact-strip span {
    writing-mode: vertical-rl; transform: rotate(180deg);
    font-size: 20px; line-height: 1; white-space: nowrap;
  }
  .strip-heading { left: 304px; width: 57px; background: var(--strip-red); }
  .strip-heading span { color: var(--strip-red-ink); font-size: 27px; letter-spacing: 0.5px; }
  .strip-fax { left: 363px; width: 57px; background: var(--strip-yellow); }
  .strip-fax span { color: var(--strip-yellow-ink); }
  .strip-email { left: 421px; width: 56px; background: var(--strip-sky); }
  .strip-email span { color: var(--strip-sky-ink); }

  .sender-address {
    position: absolute; left: 498px; top: 46px;
    color: var(--paper); font-size: 28px; line-height: 37.5px; font-style: normal;
  }
  .sender-address strong { font-weight: 700; }

  .stamp {
    position: absolute; left: 973px; top: 32px; width: 197px; height: 218px;
    background: radial-gradient(ellipse at center, var(--stamp-cream) 0%, #e9a08f 45%, var(--stamp-red) 80%);
    border: 6px solid var(--paper);
    outline: 1px solid #eee;
  }

  .recipient-label {
    position: absolute; left: 711px; top: 370px;
    color: var(--ink); font-size: 27px;
  }
  .barcode-label {
    position: absolute; left: 517px; top: 836px;
    color: var(--ink); font-size: 27px;
  }
</style>
</head>
<body>
<main class="postcard">
  <header class="header-band">
    <div class="brand-box">
      <div class="brand-mark"></div>
      <div class="brand-name">Veltra Pro</div>
    </div>
    <div class="contact-strip strip-heading"><span>CONTACT US</span></div>
    <div class="contact-strip strip-fax"><span>Fax: +1 (877) 555.0142</span></div>
    <div class="contact-strip strip-email"><span>Email: info@veltrapro.com</span></div>
    <address class="sender-address">
      Veltra Pro, LLC<br>
      4820 Harbor Ridge Road<br>
      Suite 410-275<br>
      Brookfield, GA 30190 - U.S.A.<br>
      <strong>Phone:</strong> +1 (404) 555.0187
    </address>
  </header>

  <div class="stamp" role="img" aria-label="Red two-cent postage stamp with a portrait"></div>

  <p class="recipient-label">Recipient Mailing Address</p>
  <p class="barcode-label">Barcode Area</p>
</main>
</body>
</html>
```